Smooth on the Corner needs a new flyer

Smooth on the Corner focuses on waxing and is a male and female wax studio (him & her) with colours light grey red white .or open to unisex colours but obviously need to stick to logo attached.. My theme is fun & funky ,.I am thinking cover page and prices on back.i have images that is going on my new website but not sure if i want to keep it easy to focus on prices?
this will go on front ....
First time guest?
Enjoy a complimentry wax ...
for her- indulge in a brow,underarm or bikini line wax
for him-go smooth with a free ear,nose or brow wax

Target Market(s)

18-35

Industry/Entity Type

Beauty Salon

Font styles to use
Sans Serif

Colors
ec1f27
d5d5d5
ffffff

Requirements
Must have
• light grey red and white , fun, unisex
Nice to have
• wow factor
Should not have
• clinical beauty salon feel/ do not favor my current website, i am having it re-done in a fun way.

```html
<!DOCTYPE html>
<html lang="en">
<head>
<meta charset="utf-8">
<title>Smooth on the Corner – First Time Guest Flyer</title>
<link rel="stylesheet" href="https://fonts.googleapis.com/css2?family=Tinos:wght@700&family=Open+Sans:wght@600&display=swap">
<style>
  :root {
    --brand-red: #ec1f27;
    --deep-red: #c8141c;
    --light-grey: #d5d5d5;
    --silver: #bdbdbd;
    --white: #ffffff;
    --blush: #f6e4e6;
    --ink: #111111;
  }
  html, body {
    margin: 0;
    padding: 0;
    width: 900px;
    height: 1200px;
    overflow: hidden;
    background: var(--white);
  }
  .flyer {
    position: relative;
    width: 900px;
    height: 1200px;
    overflow: hidden;
    background: linear-gradient(160deg, var(--white) 0%, var(--blush) 55%, #f1d9dc 100%);
  }
  .flyer__shapes {
    position: absolute;
    inset: 0;
  }
  .brand-name {
    position: absolute;
    left: 40px;
    top: 272px;
    width: 340px;
    margin: 0;
    font-family: "Open Sans", Arial, sans-serif;
    font-weight: 600;
    font-size: 50px;
    line-height: 1.04;
    color: var(--brand-red);
    letter-spacing: -1px;
  }
  .offer {
    position: absolute;
    right: 34px;
    top: 640px;
    width: 500px;
    text-align: right;
    font-family: "Tinos", "Times New Roman", serif;
    font-weight: 700;
  }
  .offer__title {
    margin: 0 0 10px;
    font-size: 52px;
    line-height: 1.1;
    color: var(--ink);
    text-align: left;
  }
  .offer__line {
    margin: 0;
    font-size: 28px;
    line-height: 1.32;
    color: var(--brand-red);
  }
</style>
</head>
<body>
<main class="flyer">
  <svg class="flyer__shapes" width="900" height="1200" viewBox="0 0 900 1200">
    <defs>
      <linearGradient id="silver-disc" x1="0" y1="0" x2="1" y2="1">
        <stop offset="0" stop-color="#f4f4f4"/>
        <stop offset="0.5" stop-color="#d5d5d5"/>
        <stop offset="1" stop-color="#a9a9a9"/>
      </linearGradient>
      <linearGradient id="skin-back" x1="0" y1="0" x2="1" y2="1">
        <stop offset="0" stop-color="#e9c3ad"/>
        <stop offset="1" stop-color="#c9957c"/>
      </linearGradient>
      <linearGradient id="portrait-tone" x1="0" y1="0" x2="1" y2="1">
        <stop offset="0" stop-color="#3a2a26"/>
        <stop offset="1" stop-color="#d9b7a2"/>
      </linearGradient>
      <linearGradient id="leg-tone" x1="0" y1="0" x2="1" y2="1">
        <stop offset="0" stop-color="#f3e7e4"/>
        <stop offset="1" stop-color="#d6b3a6"/>
      </linearGradient>
    </defs>

    <polygon class="panel-soft" points="0,0 900,0 900,100 0,250" fill="#ffffff" opacity="0.7"/>
    <polygon class="panel-soft" points="0,1200 0,900 900,1080 900,1200" fill="#f0d3d7" opacity="0.6"/>

    <polygon class="band band--top" points="0,180 900,40 900,110 0,235" fill="var(--brand-red)"/>
    <polygon class="band band--top-thin" points="0,250 900,122 900,132 0,260" fill="var(--deep-red)" opacity="0.35"/>

    <polygon class="band band--bottom" points="0,1040 520,1200 330,1200 0,1100" fill="var(--brand-red)"/>
    <polygon class="band band--bottom-right" points="900,1120 900,1200 700,1200" fill="var(--brand-red)"/>

    <circle class="disc" cx="450" cy="118" r="66" fill="url(#silver-disc)" stroke="#ffffff" stroke-width="6"/>
    <circle class="disc" cx="450" cy="1010" r="66" fill="url(#silver-disc)" stroke="#ffffff" stroke-width="6"/>

    <circle class="photo-ring" cx="660" cy="440" r="214" fill="var(--brand-red)"/>
    <circle class="photo-ring" cx="660" cy="440" r="204" fill="var(--white)"/>
    <circle class="photo" cx="660" cy="440" r="196" fill="url(#skin-back)" role="img" aria-label="Photo of a wax strip being applied to a client's back"/>

    <circle class="photo-ring" cx="225" cy="535" r="138" fill="var(--brand-red)"/>
    <circle class="photo-ring" cx="225" cy="535" r="129" fill="var(--white)"/>
    <circle class="photo" cx="225" cy="535" r="122" fill="url(#portrait-tone)" role="img" aria-label="Portrait photo of a smiling client"/>

    <circle class="photo-ring" cx="225" cy="872" r="160" fill="var(--brand-red)"/>
    <circle class="photo-ring" cx="225" cy="872" r="151" fill="var(--white)"/>
    <circle class="photo" cx="225" cy="872" r="143" fill="url(#leg-tone)" role="img" aria-label="Photo of a wax strip being removed from a client's leg"/>
  </svg>

  <h1 class="brand-name">Smooth on the Corner</h1>

  <section class="offer">
    <h2 class="offer__title">First time guest?</h2>
    <p class="offer__line">Enjoy a complimentry wax ...</p>
    <p class="offer__line">for her- indulge in a brow,underarm</p>
    <p class="offer__line">or bikini line wax</p>
    <p class="offer__line">for him-go smooth with a free ear,nose</p>
    <p class="offer__line">or brow wax</p>
  </section>
</main>
</body>
</html>
```